Brightwave Business Card

Professional Business Card Design required using the attached contact information.

Contact information can be rearranged as required.

The company is a new start up venture developing solar systems, the branding should be in keeping with that of one of the investors whose website is as follows https://www.quorvex.com/

```html
<!DOCTYPE html>
<html lang="en">
<head>
<meta charset="UTF-8">
<title>Brightwave Business Card</title>
<link rel="stylesheet" href="https://fonts.googleapis.com/css2?family=Source+Sans+3:wght@400;600;700&display=swap">
<style>
  :root {
    --canvas: #e6e7e7;
    --card-dark: #161616;
    --card-light: #f4f4f4;
    --ink: #2a2a2a;
    --ink-soft: #d8d8d8;
    --brand-green: #2b6a55;
  }
  * { box-sizing: border-box; margin: 0; padding: 0; }
  html, body {
    width: 1200px;
    height: 960px;
    overflow: hidden;
    background: var(--canvas);
    font-family: "Source Sans 3", "Source Sans Pro", sans-serif;
  }
  .stage { position: relative; width: 1200px; height: 960px; }
  .card {
    position: absolute;
    left: 302px;
    width: 600px;
    height: 342px;
  }
  .card--front { top: 114px; background: var(--card-dark); }
  .card--back { top: 509px; background: var(--card-light); color: var(--ink); }

  .front-url {
    position: absolute;
    left: 54px;
    top: 160px;
    font-size: 15px;
    color: var(--ink-soft);
    letter-spacing: 0.1px;
  }

  .wordmark {
    position: absolute;
    right: 43px;
    top: 44px;
    font-size: 20px;
    font-weight: 600;
    letter-spacing: 2px;
    color: var(--ink);
    text-transform: uppercase;
  }

  .holder {
    position: absolute;
    right: 43px;
    top: 141px;
    font-size: 20px;
    font-weight: 700;
    color: var(--brand-green);
    letter-spacing: 0.3px;
    text-transform: uppercase;
  }

  .company-block {
    position: absolute;
    right: 43px;
    top: 199px;
    text-align: right;
    font-size: 15px;
    line-height: 21px;
  }
  .company-name { color: var(--brand-green); }

  .contact-list {
    position: absolute;
    right: 43px;
    top: 248px;
    list-style: none;
    font-size: 15px;
    line-height: 20px;
    text-align: right;
  }
  .contact-list li {
    display: flex;
    justify-content: flex-end;
    align-items: center;
    gap: 4px;
  }
  .contact-icon { width: 13px; height: 13px; fill: var(--brand-green); flex: none; }
</style>
</head>
<body>
<main class="stage">
  <section class="card card--front" aria-label="Card front">
    <p class="front-url">www.brightwave-renewables.com</p>
  </section>

  <section class="card card--back" aria-label="Card back">
    <p class="wordmark">Brightwave Renewables</p>
    <h1 class="holder">Daniel Corvell</h1>
    <div class="company-block">
      <p class="company-name">Brightwave Renewables LLC</p>
      <p class="company-address">318 Harbor Street, Boston, MA 02110</p>
    </div>
    <ul class="contact-list">
      <li>+1 (555) 014-2786
        <svg class="contact-icon" viewBox="0 0 16 16" aria-hidden="true"><path d="M3.6 1l2.3 3-1.3 1.7c.8 1.9 2.4 3.6 4.4 4.5l1.7-1.3 3 2.3-1.3 2.6C7 13.5 2.5 9 1.2 2.3z"/></svg>
      </li>
      <li>daniel.corvell@brightwave-renewables.com
        <svg class="contact-icon" viewBox="0 0 16 16" aria-hidden="true"><path d="M1 3h14v10H1zM2.5 4.5v.4L8 9l5.5-4.1v-.4zM2.5 6.7v4.8h11V6.7L8 10.8z"/></svg>
      </li>
      <li>www.brightwave-renewables.com
        <svg class="contact-icon" viewBox="0 0 16 16" aria-hidden="true"><path d="M8 1a7 7 0 100 14A7 7 0 008 1zm0 1.4c.7.6 1.3 1.9 1.6 3.6H6.4C6.7 4.3 7.3 3 8 2.4zM5.2 3.1C4.9 3.9 4.6 4.9 4.5 6H2.8a5.6 5.6 0 012.4-2.9zM2.5 7.4h1.9v1.2H2.5zm.3 2.6h1.7c.1 1.1.4 2.1.7 2.9A5.6 5.6 0 012.8 10zM8 13.6c-.7-.6-1.3-1.9-1.6-3.6h3.2c-.3 1.7-.9 3-1.6 3.6zm-2.1-5V7.4h4.2v1.2zm4.9 4.3c.3-.8.6-1.8.7-2.9h1.7a5.6 5.6 0 01-2.4 2.9zm1.8-4.3V7.4h1.9v1.2zM11.5 6c-.1-1.1-.4-2.1-.7-2.9A5.6 5.6 0 0113.2 6z"/></svg>
      </li>
    </ul>
  </section>
</main>
</body>
</html>
```